Business Card Design Project

Thornwick Property Management

Our Business is residential property management, we therefore need a card that displays a professional image, but is clear and concise, and easy to read
Updates

We are committed now guys and girls, loving what we are seeing so far! 

Target Market(s)

Landlords, Rental Property Owners

Industry/Entity Type

Residential

Requirements
Must have
• Dale Thornwick - Principal
Fiona Thornwick - Director (Property Management)

PO Box 817
Pellworth SA 5193

Dale: 0490 367 258
Fiona: 0490 723 519

www.thornwickpropertymanagement.com.au
admin@thornwickpropertymanagement.com.au

Nice to have
• I would like the card to be double sided, white background on the information side and then colour on the reverse, in blue or black and incorporating our logo

```html
<!DOCTYPE html>
<html lang="en">
<head>
<meta charset="utf-8">
<title>Thornwick Property Management — Business Card</title>
<link rel="stylesheet" href="https://fonts.googleapis.com/css2?family=Source+Sans+3:wght@400;600;700&display=swap">
<style>
  :root {
    --backdrop: #e8e5e0;
    --card-white: #ffffff;
    --charcoal: #58595b;
    --text-dark: #3d3d3f;
    --brand-blue: #1667b0;
    --band-grey: #6d6e71;
    --back-grey: #58595b;
  }
  * { margin: 0; padding: 0; box-sizing: border-box; }
  html, body {
    width: 1200px; height: 1049px; overflow: hidden;
    background: var(--backdrop);
    font-family: "Source Sans 3", "Segoe UI", sans-serif;
  }
  .stage { position: relative; width: 1200px; height: 1049px; }
  .card {
    position: absolute; width: 764px; height: 438px;
    overflow: hidden;
    box-shadow: 0 3px 10px rgba(0,0,0,.22);
  }
  .card--front { left: 77px; top: 61px; background: var(--card-white); }
  .card--back { left: 358px; top: 541px; background: var(--back-grey); }

  .brand {
    position: absolute; display: flex; align-items: center; gap: 22px;
    left: 50%; transform: translateX(-50%);
    white-space: nowrap;
  }
  .brand__mark {
    width: 86px; height: 86px; border-radius: 6px;
    background: var(--brand-blue);
  }
  .brand__name {
    font-weight: 700; line-height: 1;
    display: flex; flex-direction: column;
  }
  .brand__name-main { font-size: 70px; letter-spacing: -1px; }
  .brand__name-sub { font-size: 24px; margin-top: 4px; align-self: flex-end; }
  .card--front .brand { top: 42px; }
  .card--front .brand__name { color: var(--charcoal); }
  .card--back .brand { top: 140px; }
  .card--back .brand__name { color: #ffffff; }

  .contacts {
    position: absolute; top: 188px; left: 0; width: 100%;
    text-align: center; color: var(--text-dark);
  }
  .person { font-size: 19px; line-height: 34px; display: flex; justify-content: center; align-items: center; }
  .person__name { color: var(--brand-blue); font-weight: 700; font-size: 24px; margin-right: 6px; }
  .person__divider { width: 1px; height: 20px; background: #b5b6b8; margin: 0 9px; }
  .icon { width: 14px; height: 14px; margin-right: 6px; fill: var(--text-dark); }
  .links { margin-top: 14px; }
  .link { font-size: 19px; line-height: 29px; display: flex; justify-content: center; align-items: center; }

  .footer-rule {
    position: absolute; left: 0; right: 0; top: 376px;
    height: 4px; background: var(--brand-blue);
  }
  .footer-band {
    position: absolute; left: 0; right: 0; bottom: 0; height: 50px;
    background: var(--band-grey);
    display: flex; align-items: center; justify-content: flex-end;
    padding-right: 22px;
  }
  .address { color: #ffffff; font-size: 21px; }
  .back-web {
    position: absolute; top: 345px; left: 0; width: 100%;
    text-align: center; color: #ffffff; font-size: 19px; letter-spacing: 2px;
  }
</style>
</head>
<body>
<main class="stage">
  <section class="card card--front" aria-label="Card front">
    <div class="brand">
      <span class="brand__mark"></span>
      <span class="brand__name"><span class="brand__name-main">Thornwick</span><span class="brand__name-sub">Property Management</span></span>
    </div>
    <div class="contacts">
      <p class="person"><span class="person__name">Dale Thornwick,</span>Principal<span class="person__divider"></span>
        <svg class="icon" viewBox="0 0 24 24"><path d="M6.6 10.8c1.4 2.8 3.8 5.1 6.6 6.6l2.2-2.2c.3-.3.7-.4 1-.2 1.1.4 2.3.6 3.6.6.6 0 1 .4 1 1V20c0 .6-.4 1-1 1C10.6 21 3 13.4 3 4c0-.6.4-1 1-1h3.5c.6 0 1 .4 1 1 0 1.3.2 2.5.6 3.6.1.3 0 .7-.2 1z"/></svg>0490 367 258</p>
      <p class="person"><span class="person__name">Fiona Thornwick,</span>Director<span class="person__divider"></span>
        <svg class="icon" viewBox="0 0 24 24"><path d="M6.6 10.8c1.4 2.8 3.8 5.1 6.6 6.6l2.2-2.2c.3-.3.7-.4 1-.2 1.1.4 2.3.6 3.6.6.6 0 1 .4 1 1V20c0 .6-.4 1-1 1C10.6 21 3 13.4 3 4c0-.6.4-1 1-1h3.5c.6 0 1 .4 1 1 0 1.3.2 2.5.6 3.6.1.3 0 .7-.2 1z"/></svg>0490 723 519</p>
      <div class="links">
        <p class="link"><svg class="icon" viewBox="0 0 24 24"><path d="M2 5h20v14H2z M2 5l10 7 10-7" /></svg>admin@thornwickpropertymanagement.com.au</p>
        <p class="link"><svg class="icon" viewBox="0 0 24 24"><circle cx="12" cy="12" r="10"/></svg>www.thornwickpropertymanagement.com.au</p>
      </div>
    </div>
    <div class="footer-rule"></div>
    <div class="footer-band"><p class="address">PO Box 817, Pellworth SA 5193</p></div>
  </section>

  <section class="card card--back" aria-label="Card back">
    <div class="brand">
      <span class="brand__mark"></span>
      <span class="brand__name"><span class="brand__name-main">Thornwick</span><span class="brand__name-sub">Property Management</span></span>
    </div>
    <p class="back-web">www.thornwickpropertymanagement.com.au</p>
  </section>
</main>
</body>
</html>
```